Thank You Card

I'm looking for a thank you card design using our logo and other graphics. We are an essential business and our employees (Electricians) have done an incredible job staying healthy and safe during the COVID-19 pandemic, I want to send each a thank you card.

```html
<!DOCTYPE html>
<html lang="en">
<head>
<meta charset="utf-8">
<title>Thank You Card</title>
<link href="https://fonts.googleapis.com/css2?family=Bebas+Neue&family=Libre+Baskerville:wght@700&display=swap" rel="stylesheet">
<style>
  :root {
    --navy: #16445c;
    --navy-pattern: #2a5870;
    --red: #f4262f;
    --white: #ffffff;
  }
  * { margin: 0; padding: 0; box-sizing: border-box; }
  html, body { width: 1200px; height: 732px; overflow: hidden; background: var(--navy); }
  .card {
    position: relative;
    width: 1200px;
    height: 732px;
    background: var(--navy);
    overflow: hidden;
  }
  .pattern-band {
    position: absolute;
    left: 0;
    width: 1200px;
    background: linear-gradient(180deg, var(--navy-pattern), #24526a);
  }
  .pattern-band--top { top: 0; height: 83px; }
  .pattern-band--bottom { top: 440px; height: 292px; }
  .headline {
    position: absolute;
    left: 0;
    top: 62px;
    width: 1200px;
    text-align: center;
    font-family: "Bebas Neue", "Oswald", sans-serif;
    font-size: 340px;
    line-height: 1;
    color: var(--white);
    letter-spacing: 2px;
    text-shadow: 3px 3px 0 var(--red), 6px 5px 0 var(--red), 8px 7px 0 var(--red);
    transform: scaleX(0.86);
    transform-origin: 52% 50%;
    white-space: nowrap;
  }
  .ribbon {
    position: absolute;
    left: 229px;
    top: 352px;
    width: 750px;
    height: 74px;
  }
  .ribbon svg { display: block; }
  .ribbon__text {
    position: absolute;
    inset: 0;
    display: flex;
    align-items: center;
    justify-content: center;
    font-family: "Libre Baskerville", Georgia, serif;
    font-weight: 700;
    font-size: 44px;
    color: var(--white);
    padding-bottom: 4px;
  }
  .brand-box {
    position: absolute;
    left: 438px;
    top: 500px;
    width: 350px;
    height: 174px;
    background: var(--white);
    display: flex;
    align-items: center;
    justify-content: center;
  }
  .brand-name {
    font-family: "Bebas Neue", "Oswald", sans-serif;
    font-size: 54px;
    line-height: 1;
    color: var(--red);
    letter-spacing: 1px;
  }
</style>
</head>
<body>
  <main class="card">
    <div class="pattern-band pattern-band--top" role="img" aria-label="Repeating pattern of small outlined hearts"></div>
    <div class="pattern-band pattern-band--bottom" role="img" aria-label="Repeating pattern of small outlined hearts"></div>

    <h1 class="headline">THANK YOU</h1>

    <div class="ribbon">
      <svg width="750" height="74" viewBox="0 0 750 74" aria-hidden="true">
        <polygon points="0,74 48,37 28,0 722,0 702,37 750,74" fill="var(--red)"/>
      </svg>
      <p class="ribbon__text">For all your dedication!</p>
    </div>

    <div class="brand-box">
      <span class="brand-name">Brightline Electric Co.</span>
    </div>
  </main>
</body>
</html>
```